Vantrelo App Homepage Design making customers feel in control of their spend

Hi,
We need a App Homepage design with a UI similar to the attached mock up on an Quorix 4. The app is intended to put customers in control of their usage and spend on their fixed phone, broadband, mobile, gas and electricity.

Please fee free to propose improvements to the background images, icons, colours, etc.

Any questions please let me know.

Thanks
Bertram

Target Market(s)

Consumer customers

Industry/Entity Type

Internet

Font styles to use
Sans Serif

Colors
3276b5
0255a3
85acd3
cfdeed
ffffff

Requirements
Must have
• Content in line with the guidelines in the attached mock up

```html
<!DOCTYPE html>
<html lang="en">
<head>
<meta charset="utf-8">
<title>Vantrelo – Home</title>
<link href="https://fonts.googleapis.com/css2?family=Nunito:wght@400;600;700&display=swap" rel="stylesheet">
<style>
  :root{
    --bg:#e6ebf1;
    --header:#cfdeed;
    --hero-top:#3276b5;
    --hero-bottom:#1f8fc4;
    --brand:#0255a3;
    --icon-soft:#3a8fd6;
    --white:#ffffff;
    --row-line:#e4e7ea;
    --label:#6f7479;
    --calls:#1e7fd1;
    --electricity:#f0474f;
    --gas:#f7941d;
    --mobile:#1fbf3a;
    --fibra:#ee3fc0;
    --support:#1fc24a;
    --footer:#0255a3;
    --avatar:#c98a62;
  }
  *{box-sizing:border-box;margin:0;padding:0}
  html,body{width:1200px;height:1200px;overflow:hidden}
  body{background:var(--bg);font-family:'Nunito',sans-serif;display:flex;align-items:center;justify-content:center}
  .screen{width:620px;height:1110px;background:var(--white);display:flex;flex-direction:column;box-shadow:0 20px 50px rgba(2,85,163,.15)}

  .app-header{height:97px;background:var(--header);display:flex;align-items:center;justify-content:space-between;padding:0 22px}
  .app-header svg{width:38px;height:38px}
  .brand{display:flex;align-items:center;gap:10px;font-weight:700;font-size:30px;color:var(--brand)}
  .brand-dot{width:26px;height:26px;border-radius:50%;background:var(--brand)}

  .hero{height:433px;position:relative;background:linear-gradient(160deg,var(--hero-top),var(--hero-bottom) 60%,#2aa0d0)}
  .hero-photo{position:absolute;inset:0;background:radial-gradient(circle at 72% 45%,rgba(255,255,255,.14),transparent 45%)}
  .greeting{position:absolute;top:30px;left:0;right:0;text-align:center;color:var(--white)}
  .avatar{width:126px;height:126px;border-radius:50%;border:5px solid var(--white);background:radial-gradient(circle at 50% 40%,#e8b090,var(--avatar) 60%,#7a4a30);margin:0 auto 14px}
  .greeting h1{font-weight:400;font-size:26px}
  .greeting h1 .name{color:var(--electricity)}
  .greeting p{font-size:18px;margin-top:2px}
  .hero-divider{position:absolute;top:242px;left:0;right:0;height:1px;background:rgba(255,255,255,.55)}
  .total{position:absolute;top:297px;left:40px;right:40px;height:82px;border-radius:41px;border:2px solid var(--white);
    background:linear-gradient(90deg,var(--calls) 0 20.6%,var(--electricity) 20.6% 52%,var(--gas) 52% 78.2%,var(--mobile) 78.2% 93%,var(--fibra) 93% 100%);
    display:flex;align-items:center;padding-left:32px;color:var(--white);font-weight:700;font-size:27px;white-space:nowrap}
  .total .amount{font-size:38px;margin-left:12px;font-weight:600}

  .charges{list-style:none}
  .charge{height:71.6px;border-bottom:1px solid var(--row-line);display:flex;align-items:center;padding:0 28px 0 24px;font-size:25px}
  .charge svg{width:32px;height:32px;margin-right:18px}
  .charge .label{color:var(--label);font-weight:600;flex:1}
  .charge .value{font-weight:600}
  .calls .value{color:var(--calls)} .electricity .value{color:var(--electricity)}
  .gas .value{color:var(--gas)} .mobile .value{color:var(--mobile)} .fibra .value{color:var(--fibra)}

  .support-area{flex:1;display:flex;align-items:center;justify-content:center}
  .support-btn{width:267px;height:75px;border-radius:38px;background:var(--support);color:var(--white);font-size:26px;display:flex;align-items:center;justify-content:center;gap:12px}
  .support-btn svg{width:34px;height:34px}

  .footer{height:83px;background:var(--footer);color:var(--white);text-align:center;font-weight:600;font-size:24px;line-height:1.3;display:flex;flex-direction:column;justify-content:center}
</style>
</head>
<body>
<main class="screen">
  <header class="app-header">
    <svg viewBox="0 0 24 24" fill="none" stroke="var(--icon-soft)" stroke-width="1.4" aria-label="Settings">
      <circle cx="12" cy="12" r="3.2"/>
      <circle cx="12" cy="12" r="8" stroke-dasharray="3.2 3.08" stroke-width="3"/>
      <circle cx="12" cy="12" r="6.3"/>
    </svg>
    <div class="brand"><span class="brand-dot"></span>Vantrelo</div>
    <svg viewBox="0 0 24 24" fill="none" stroke="var(--icon-soft)" stroke-width="1.6" stroke-linecap="round" aria-label="Menu">
      <path d="M3 7h18M3 12h18M3 17h18"/>
    </svg>
  </header>

  <section class="hero">
    <div class="hero-photo" role="img" aria-label="Background photo of a person relaxing with headphones, tinted blue"></div>
    <div class="greeting">
      <div class="avatar" role="img" aria-label="Profile photo of Marisol"></div>
      <h1>Good morning, <span class="name">Marisol</span></h1>
      <p>Welcome to Vantrelo</p>
    </div>
    <div class="hero-divider"></div>
    <div class="total">You current total charges: <span class="amount">£ 68.39</span></div>
  </section>

  <ul class="charges">
    <li class="charge calls">
      <svg viewBox="0 0 24 24" fill="var(--calls)"><path d="M6.6 2.5l2.6 3.6c.4.6.3 1.3-.2 1.8L7.6 9.2c1.2 2.8 4.3 6 7.2 7.2l1.3-1.4c.5-.5 1.2-.6 1.8-.2l3.6 2.6c.6.4.7 1.2.3 1.8l-1.4 2c-.6.8-1.6 1.2-2.6.9C10.6 20 4 13.4 1.9 6.2c-.3-1 .1-2 .9-2.6l2-1.4c.6-.4 1.4-.3 1.8.3z"/></svg>
      <span class="label">Calls</span><span class="value">£ 14.80</span>
    </li>
    <li class="charge electricity">
      <svg viewBox="0 0 24 24" fill="var(--electricity)"><path d="M12 2a7 7 0 0 0-4 12.7V17h8v-2.3A7 7 0 0 0 12 2z"/><rect x="8.5" y="18.2" width="7" height="1.8" rx=".9"/><rect x="9.5" y="21" width="5" height="1.8" rx=".9"/></svg>
      <span class="label">Electricity</span><span class="value">£ 21.00</span>
    </li>
    <li class="charge gas">
      <svg viewBox="0 0 24 24" fill="var(--gas)"><path d="M12 2c1 4 6 6 6 12a6 6 0 0 1-12 0c0-3 1.5-4.5 2.5-6 .3 2 1 3 2 3.5C10 8 11 5 12 2z"/></svg>
      <span class="label">Gas</span><span class="value">£ 20.90</span>
    </li>
    <li class="charge mobile">
      <svg viewBox="0 0 24 24" fill="none" stroke="var(--mobile)" stroke-width="2"><rect x="7" y="2.5" width="10" height="19" rx="1.5"/></svg>
      <span class="label">Mobile</span><span class="value">£ 8.10</span>
    </li>
    <li class="charge fibra">
      <svg viewBox="0 0 24 24" fill="none" stroke="var(--fibra)" stroke-width="2.4" stroke-linecap="round"><path d="M2 9a14 14 0 0 1 20 0M5.5 12.5a9 9 0 0 1 13 0M9 16a4 4 0 0 1 6 0"/><circle cx="12" cy="19.5" r="1.4" fill="var(--fibra)" stroke="none"/></svg>
      <span class="label">Fibra</span><span class="value">£ 3.59</span>
    </li>
  </ul>

  <div class="support-area">
    <div class="support-btn">
      <svg viewBox="0 0 24 24" fill="none" stroke="var(--white)" stroke-width="1.5" stroke-linecap="round"><circle cx="12" cy="9" r="4.5"/><path d="M6.5 9a5.5 5.5 0 0 1 11 0M4 22c.5-4 3.8-6.5 8-6.5s7.5 2.5 8 6.5z"/></svg>
      24/7 Support
    </div>
  </div>

  <footer class="footer">
    <span>Last bill: £ 75.76 on 9/12/2016</span>
    <span>Allowence renews in 18 days</span>
  </footer>
</main>
</body>
</html>
```